Manufacturer's Representative Group needs a clean new Website

We represent and sell a number of suppliers that design and build products used in Biopharmaceutical manufacturing. Our sales region is in the central US. Our customer base is scientific / engineering based - so clean, we organized design with a focus on the products - easy and clear navigation is necessary. We do not sell direct or warehouse product - so e-commerce is not needed. Our customers will use the website for reference on what we do and offer - we will use the site as a platform to present products from each vendor and the home page will be used to capture an overview and draw users deeper into the site. You can view our current site - which needs A LOT of help to get ideas on products represented and types of products

Target Market(s)

Engineers and Pharmaceutical / Bio pharm end users

Industry/Entity Type

E-Commerce

Number of Pages Required

2 page

Font styles to use
Sans Serif

Requirements
Must have
• I need a home page that provides a snapshot of my company and the product lines we represent - then a second page that I can copy as a template for each line I rep as well as for an "About us / contact" page.
• I would like to be able to manage content on the pages so something easy to adjust pictures or add content is a must
• Must use our logo

```html
<!DOCTYPE html>
<html lang="en">
<head>
<meta charset="utf-8">
<title>Prairie Bio</title>
<link rel="stylesheet" href="https://fonts.googleapis.com/css2?family=Exo+2:ital,wght@1,700;1,800&family=Open+Sans:wght@400;600;700&family=Passion+One&family=Questrial&display=swap">
<style>
:root{
  --navy:#262463;
  --orange:#f05a28;
  --ink:#333;
  --muted:#555;
  --bg:#e4e4e4;
  --bar:#2e2e2e;
  --card-frame:#a9acb0;
}
*{margin:0;padding:0;box-sizing:border-box}
html,body{width:1103px;height:1200px;overflow:hidden}
body{background:var(--bg);font-family:Arial,Helvetica,sans-serif;color:var(--ink)}
.page{position:relative;width:1200px;height:1305px;transform:scale(.91917);transform-origin:0 0;
  background:radial-gradient(ellipse at 50% 30%,#f7f7f7 0%,#ebebeb 55%,#dedede 100%)}
.abs{position:absolute}

/* header */
.brand{left:118px;top:38px;display:flex;align-items:center;gap:16px}
.brand-dot{width:34px;height:34px;border-radius:50%;background:var(--orange)}
.brand-name{font-family:'Open Sans',sans-serif;font-weight:600;font-size:50px;color:var(--navy);letter-spacing:-1px}
.call{left:948px;top:32px}
.call-title{font-family:'Exo 2',sans-serif;font-style:italic;font-weight:700;font-size:24px;color:var(--navy)}
.call-phone{font-family:'Questrial',sans-serif;font-size:20px;color:#444;line-height:25px}

/* nav */
.nav-home{left:103px;top:135px;width:102px;height:40px;background:var(--orange);
  clip-path:polygon(12px 0,100% 0,100% 100%,0 100%);display:flex;align-items:center;padding-left:22px;gap:7px;
  color:#fff;font-size:13px;font-family:'Open Sans',sans-serif}
.nav-main{left:204px;top:135px;width:390px;height:40px;background:var(--navy);display:flex;align-items:center;padding-left:22px}
.nav-main a{color:#fff;text-decoration:none;font-family:'Open Sans',sans-serif;font-size:13px;padding:0 25px;border-left:1px solid #3d3b80;line-height:18px}
.nav-main a:last-child{border-right:1px solid #3d3b80}
.updates{left:594px;top:135px;width:497px;height:40px;background:var(--orange);
  clip-path:polygon(0 0,100% 0,calc(100% - 16px) 100%,0 100%);display:flex;align-items:center;padding-left:14px;color:#fff}
.updates b{font-family:'Passion One',sans-serif;font-weight:400;font-size:20px;margin-right:6px;letter-spacing:.5px}
.updates span{font-size:12px}

/* hero */
.hero-image{left:110px;top:195px;width:480px;height:420px;border-radius:8px;
  background:radial-gradient(ellipse at 45% 50%,#c9c9cc 0%,#e8e8ea 55%,rgba(240,240,240,0) 75%)}
.hero-title{left:628px;top:248px;font-family:'Exo 2',sans-serif;font-style:italic;font-weight:800;font-size:46px;line-height:56px;color:#333}
.hero-title em{color:var(--navy);font-style:italic}
.hero-text{left:629px;top:371px;width:455px;font-size:13px;line-height:20px;color:#222}
.btn-learn{left:631px;top:448px;width:218px;height:51px;background:#2f2f2f;border:1px solid #555;
  color:#fff;font-family:'Passion One',sans-serif;font-size:29px;display:flex;align-items:center;justify-content:center;letter-spacing:.5px}
.divider{left:105px;top:638px;width:990px;height:22px;
  background:radial-gradient(ellipse at 50% 0,rgba(0,0,0,.22) 0%,rgba(0,0,0,0) 70%)}

/* products */
.section-title{left:118px;top:690px;font-family:'Open Sans',sans-serif;font-weight:700;font-size:31px;color:#333}
.section-title span{color:var(--orange)}
.arrow{top:807px;width:39px;height:40px;background:#a8a8a8;display:flex;align-items:center;justify-content:center}
.product{top:760px;width:199px}
.product-photo{height:126px;border:2px solid var(--card-frame);
  background:linear-gradient(180deg,#5c95cf 0%,#8fb8e0 45%,#d9dde2 75%,#c4c6c9 100%)}
.product-label{margin-top:4px;height:29px;background:#333;color:#fff;font-family:'Open Sans',sans-serif;font-size:15px;
  display:flex;align-items:center;justify-content:center}

/* info boxes */
.box{top:990px;width:307px;height:236px;border:1px solid #c9c9c9;border-radius:7px;
  background:linear-gradient(180deg,#fff 0%,#f1f1f1 100%);box-shadow:0 1px 3px rgba(0,0,0,.12)}
.box h2{font-family:'Questrial',sans-serif;font-weight:400;font-size:24px;color:#333;letter-spacing:.3px;padding:8px 0 0 14px}
.about-text{padding:8px 20px 0 18px;font-size:12.4px;line-height:18px;color:#444}
.about-text b{color:#333}
.partners{display:grid;grid-template-columns:1fr 1fr;row-gap:22px;padding:22px 24px 0 28px}
.partner{font-family:'Open Sans',sans-serif;font-weight:700;font-size:15px;color:#1f6fb5;height:30px;display:flex;align-items:center}
.news-form{padding:8px 18px 0 17px}
.field{height:31px;border:1px solid #ccc;border-radius:14px;background:#fff;font-size:12.5px;color:#333;padding:9px 0 0 13px;margin-bottom:7px}
.field.tall{height:59px;margin-bottom:9px}
.btn-submit{margin-left:193px;width:78px;height:34px;border-radius:6px;background:linear-gradient(#f77a40,#e54d1d);
  border:1px solid #d6461b;color:#fff;font-family:'Open Sans',sans-serif;font-size:14px;display:flex;align-items:center;justify-content:center}

/* footer */
.footer{left:0;top:1260px;width:1200px;height:45px;background:var(--bar);color:#fff;font-family:'Open Sans',sans-serif;font-size:13px}
.footer-links{position:absolute;left:117px;top:13px;display:flex;gap:12px}
.footer-links span{opacity:.9}
.copyright{position:absolute;right:120px;top:16px;font-weight:600;letter-spacing:.2px}
</style>
</head>
<body>
<div class="page">

  <header>
    <div class="abs brand"><span class="brand-dot"></span><span class="brand-name">Prairie Bio</span></div>
    <div class="abs call">
      <div class="call-title">Call us:</div>
      <div class="call-phone">(555) 014-2291</div>
      <div class="call-phone">(555) 014-7730</div>
    </div>
  </header>

  <nav>
    <div class="abs nav-home">
      <svg width="13" height="12" viewBox="0 0 13 12"><path d="M6.5 0 13 6h-2v6H8V8H5v4H2V6H0z" fill="#fff"/></svg>HOME
    </div>
    <div class="abs nav-main"><a href="#">CONTACT</a><a href="#">PRODUCTS</a></div>
    <div class="abs updates"><b>UPDATES :</b><span>Lorem Ipsum is simply dummy text of the printing and typesetting</span></div>
  </nav>

  <section class="hero">
    <div class="abs hero-image" role="img" aria-label="Laboratory microscope beside a rack of coloured test tubes and two sample vials"></div>
    <h1 class="abs hero-title"><em>PRAIRIE BIO</em> is an<br>International...</h1>
    <p class="abs hero-text">Company well known for systems in drug discovery and material science. As well as our offices in Germany, the United Kingdom, France and the USA we also have a worldwide network of distributors.</p>
    <div class="abs btn-learn">LEARN MORE</div>
    <div class="abs divider"></div>
  </section>

  <section class="products">
    <h2 class="abs section-title">Our <span>Products</span></h2>
    <div class="abs arrow" style="left:102px"><svg width="12" height="18"><path d="M10 1 2 9l8 8" fill="#fff"/></svg></div>
    <div class="abs arrow" style="left:1059px"><svg width="12" height="18"><path d="M2 1l8 8-8 8" fill="#fff"/></svg></div>
    <div class="abs product" style="left:165px"><div class="product-photo" role="img" aria-label="Automated liquid handling workstation with laptop"></div><div class="product-label">MicroSway</div></div>
    <div class="abs product" style="left:385px"><div class="product-photo" role="img" aria-label="Tray filling instrument with sample racks"></div><div class="product-label">TrayLine X &amp; FillPro</div></div>
    <div class="abs product" style="left:608px"><div class="product-photo" role="img" aria-label="Amber and clear sample bottles with coloured caps"></div><div class="product-label">VialSet Hy</div></div>
    <div class="abs product" style="left:832px"><div class="product-photo" role="img" aria-label="Automated liquid handling workstation with laptop"></div><div class="product-label">MicroSway</div></div>
  </section>

  <section>
    <div class="abs box" style="left:111px">
      <h2 style="padding-left:23px">ABOUT US</h2>
      <p class="about-text"><b>Prairie Biosolutions is a distribution channel, licensed partner</b> and manufacturers representative group providing high quality fluid handling products and technical services to the Midwestern biopharmaceutical community. With a core staff of experienced professionals and a team approach to all customer needs, we offer over 30 years of cGMP experience in the selec-tion and use of most process....</p>
    </div>
    <div class="abs box" style="left:445px">
      <h2>COMPANIES REPRESENTED</h2>
      <div class="partners">
        <div class="partner">Ridgeway Polymers</div>
        <div class="partner">Corvan Tubing Co.</div>
        <div class="partner">Flowmark</div>
        <div class="partner">Keelson</div>
        <div class="partner">CleanLine</div>
        <div class="partner">Modulo Works</div>
      </div>
    </div>
    <div class="abs box" style="left:778px">
      <h2>LATEST NEWS</h2>
      <div class="news-form">
        <div class="field">Your Name</div>
        <div class="field">Your Email</div>
        <div class="field tall">Additional Information</div>
        <div class="btn-submit">SUBMIT</div>
      </div>
    </div>
  </section>

  <footer class="abs footer">
    <div class="footer-links"><span>HOME</span><span>|</span><span>CONTACT</span><span>|</span><span>PRODUCTS</span></div>
    <div class="copyright">© PRAIRIE BIOSOLUTIONS, CORP.</div>
  </footer>

</div>
</body>
</html>
```